indépendant en tant que Massothérapeute et Préparateur Mental, j'ai besoin de ...

Massothérapeute et préparateur mental indépendant, je recherche une carte de visite sobre et dynamique, sans images liées au massage ou à la préparation mentale mais intégrant mon logo. Les couleurs que j'aime bien sont : Blanc, gris, anthracite, noir et jaune

Contact Information for Business Card

carte de préférence Horizontale
neutre qui puisse toucher le deux domaines Massothérapie et préparation mentale

Requirements
Must have
• mon projet doit intégrer au recto:
LOGO
Loïc Vermande
078 315 26 49
info@loicvermande-exemple.ch
et éventuellement www.loicvermande-exemple.ch

et au verso les deux adresses:

Chemin des Ormelets 27B
1400 Yverdon-les-Bains

Rue des Tanneries 9
1700 Fribourg

Should not have
• mon projet ne doit pas contenir d'image en liens avec le massage ni la préparation mentale.

```html
<!DOCTYPE html>
<html lang="fr">
<head>
<meta charset="utf-8">
<title>Loïc Vermande – cartes de visite</title>
<link rel="stylesheet" href="https://fonts.googleapis.com/css2?family=Montserrat:wght@400;500;600;700&display=swap">
<style>
  :root {
    --backdrop: #e6e2dc;
    --steel-dark: #7f7f80;
    --steel-mid: #959394;
    --steel-light: #a19e9f;
    --silver-1: #f4f4f4;
    --silver-2: #e2e2e2;
    --silver-3: #d4d4d4;
    --ink: #121212;
    --anthracite: #3f3f3f;
    --ink-soft: #2a2a2a;
  }
  * { margin: 0; padding: 0; box-sizing: border-box; }
  html, body { width: 1200px; height: 965px; overflow: hidden; }
  body {
    background: var(--backdrop);
    font-family: "Montserrat", sans-serif;
    position: relative;
  }
  .card {
    position: absolute;
    left: 278px;
    width: 646px;
    height: 366px;
    border-radius: 24px;
    overflow: hidden;
  }
  .card--back {
    top: 98px;
    background: linear-gradient(160deg, var(--steel-dark) 0%, var(--steel-mid) 45%, var(--steel-light) 60%, var(--steel-dark) 100%);
    color: var(--ink);
  }
  .card--front {
    top: 504px;
    background: linear-gradient(155deg, var(--silver-2) 0%, var(--silver-1) 40%, var(--silver-3) 60%, var(--silver-1) 100%);
    color: var(--ink-soft);
  }
  .brand {
    position: absolute;
    display: flex;
    align-items: center;
    gap: 14px;
  }
  .brand__dot { border-radius: 50%; flex: none; }
  .brand__name { font-weight: 600; line-height: 1; letter-spacing: 0.5px; }
  .brand__role {
    font-weight: 500;
    text-transform: uppercase;
    letter-spacing: 0.8px;
    margin-top: 5px;
  }
  .card--back .brand { left: 86px; top: 164px; }
  .card--back .brand__dot { width: 46px; height: 46px; background: var(--ink); }
  .card--back .brand__name { font-size: 30px; color: var(--ink); }
  .card--back .brand__role { font-size: 10px; color: var(--ink-soft); }
  .card--front .brand { left: 246px; top: 56px; }
  .card--front .brand__dot { width: 38px; height: 38px; background: var(--anthracite); }
  .card--front .brand__name { font-size: 25px; color: var(--anthracite); }
  .card--front .brand__role { font-size: 8.6px; color: var(--anthracite); }

  .addresses {
    position: absolute;
    left: 374px;
    top: 248px;
    font-size: 15px;
    line-height: 20px;
    color: var(--ink);
  }
  .addresses__divider {
    width: 139px;
    height: 2px;
    background: var(--ink);
    margin: 3px 0 6px;
  }

  .person { position: absolute; left: 34px; top: 200px; }
  .person__name { font-size: 24px; font-weight: 600; letter-spacing: 0.4px; color: var(--ink-soft); }
  .person__title { font-size: 14px; margin-top: 2px; color: var(--ink-soft); }
  .contacts { list-style: none; margin-top: 20px; }
  .contacts li {
    display: flex;
    align-items: center;
    gap: 10px;
    font-size: 17.5px;
    line-height: 23px;
    color: var(--ink-soft);
  }
  .contacts svg { width: 16px; height: 16px; flex: none; }
</style>
</head>
<body>

<section class="card card--back" aria-label="Verso de la carte">
  <div class="brand">
    <span class="brand__dot"></span>
    <div>
      <div class="brand__name">Loïc Vermande</div>
      <div class="brand__role">Massothérapeute / Préparateur Mental</div>
    </div>
  </div>
  <div class="addresses">
    <p>Rue des Tanneries 9<br>1700 Freiburg</p>
    <div class="addresses__divider"></div>
    <p>Chemin des Ormelets 27B<br>1400 Yverdon-les-Bains</p>
  </div>
</section>

<section class="card card--front" aria-label="Recto de la carte">
  <div class="brand">
    <span class="brand__dot"></span>
    <div>
      <div class="brand__name">Loïc Vermande</div>
      <div class="brand__role">Massothérapeute / Préparateur Mental</div>
    </div>
  </div>
  <div class="person">
    <h1 class="person__name">LOÏC VERMANDE</h1>
    <p class="person__title">Director</p>
    <ul class="contacts">
      <li>
        <svg viewBox="0 0 24 24" fill="var(--ink-soft)"><path d="M6.6 10.8a15.1 15.1 0 0 0 6.6 6.6l2.2-2.2c.3-.3.7-.4 1-.2 1.1.4 2.3.6 3.6.6.6 0 1 .4 1 1V20c0 .6-.4 1-1 1A17 17 0 0 1 3 4c0-.6.4-1 1-1h3.5c.6 0 1 .4 1 1 0 1.3.2 2.5.6 3.6.1.3 0 .7-.2 1z"/></svg>
        078 315 26 49
      </li>
      <li>
        <svg viewBox="0 0 24 24" fill="var(--ink-soft)"><path d="M2 5h20v14H2z" fill="none" stroke="var(--ink-soft)" stroke-width="2"/><path d="M2 5l10 8 10-8v2l-10 8L2 7z"/></svg>
        info@loicvermande-exemple.ch
      </li>
      <li>
        <svg viewBox="0 0 24 24" fill="none" stroke="var(--ink-soft)" stroke-width="2"><circle cx="12" cy="12" r="9.5"/><path d="M2.5 12h19M12 2.5c3 3 3 16 0 19M12 2.5c-3 3-3 16 0 19"/></svg>
        www.loicvermande-exemple.ch
      </li>
    </ul>
  </div>
</section>

</body>
</html>
```